Company Letter head for real estate company

need company letter head

You can use the logo that I submitted. no need to create a new one

• must have my address on it..38642 MARLOWE, ASHFORD, WA 48203-1957, INFO@WRKMB.CA

```html
<!DOCTYPE html>
<html lang="en">
<head>
<meta charset="utf-8">
<title>Westbrook Letterhead</title>
<link href="https://fonts.googleapis.com/css2?family=Open+Sans:wght@300;400&family=Roboto:wght@300&family=Great+Vibes&display=swap" rel="stylesheet">
<style>
  :root {
    --backdrop: #e6e6e6;
    --paper: #f3f3f3;
    --ink: #2b2b2b;
    --ink-soft: #555555;
    --brand-green: #6cbf3e;
    --scene-grey: #dcdcdc;
  }
  * { margin: 0; padding: 0; box-sizing: border-box; }
  html, body {
    width: 1200px; height: 1200px; overflow: hidden;
    background: var(--backdrop);
  }
  .letterhead {
    position: absolute; left: 190px; top: 20px;
    width: 820px; height: 1160px;
    background: var(--paper);
    font-family: "Open Sans", sans-serif;
    color: var(--ink);
  }
  .header-scene {
    position: absolute; right: 0; top: 0;
    width: 454px; height: 155px;
    background: linear-gradient(180deg, var(--scene-grey) 0%, rgba(220,220,220,0.6) 60%, rgba(243,243,243,0) 100%);
  }
  .brand {
    position: absolute; left: 79px; top: 62px;
    display: flex; align-items: center; gap: 10px;
  }
  .brand-mark { width: 22px; height: 22px; background: var(--brand-green); }
  .brand-name { font-size: 26px; font-weight: 400; letter-spacing: 1px; color: var(--ink); }
  .letter-body {
    position: absolute; left: 132px; top: 276px; width: 600px;
    font-size: 13.6px; font-weight: 300; line-height: 19.3px; color: var(--ink);
  }
  .letter-body p { margin-bottom: 19.3px; text-align: justify; }
  .salutation { margin-bottom: 19.3px; }
  .closing { margin-top: 44px; line-height: 19px; }
  .signature {
    font-family: "Great Vibes", cursive;
    font-size: 30px; line-height: 36px; margin-top: 6px; margin-left: 6px; color: var(--ink);
  }
  .footer-rule {
    position: absolute; top: 1058px; width: 106px; height: 2px;
    background: var(--brand-green);
  }
  .footer-rule.left { left: 79px; }
  .footer-rule.right { left: 635px; }
  .contact, .address {
    position: absolute; font-family: "Roboto", sans-serif;
    font-weight: 300; font-size: 13px; line-height: 16.5px; color: var(--ink-soft);
  }
  .contact { left: 79px; top: 1083px; list-style: none; }
  .contact li { display: flex; align-items: center; gap: 8px; }
  .contact svg { width: 11px; height: 11px; fill: var(--brand-green); }
  .address { right: 79px; top: 1099px; text-align: right; font-style: normal; }
</style>
</head>
<body>
  <main class="letterhead">
    <div class="header-scene" role="img" aria-label="Faint grey illustration of trees, house rooftops and a winding path"></div>

    <div class="brand">
      <span class="brand-mark"></span>
      <span class="brand-name">WESTBROOK</span>
    </div>

    <section class="letter-body">
      <div class="salutation">Dear Daniel Hartwell,</div>
      <p>Lorem ipsum dolor sit amet, consectetuer adipiscing elit, sed diam nonummy nibh euismod tincidunt ut laoreet dolore magna aliquam erat volutpat. Ut wisi enim ad minim veniam, quis nostrud exerci tation ullamcorper suscipit lobortis nisl ut aliquip ex ea commodo consequat. Duis dolore te feugait nulla facilisi. Nam liber tempor cum soluta nobis eleifend option congue nihil imperdiet doming id quod mazim placerat facer possim assum. Lorem ipsum dolor sit amet, consectetuer adipiscing elit, sed diam nonummy nibh euismod tincidunt ut laoreet dolore magna aliquam erat volutpat. Ut wisi enim ad minim veniam, quis nostrud exerci tation ullamcorper suscipit lobortis nisl ut aliquip ex ea commodo consequat.</p>
      <p>Consectetuer adipiscing elit, sed diam nonummy nibh euismod tincidunt ut laoreet dolore magna aliquam erat volutpat. Ut wisi enim ad minim veniam, quis nostrud exerci tation ullamcorper suscipit lobortis nisl ut aliquip ex ea commodo consequat. Consectetuer adipiscing elit, sed diam nonummy nibh euismod tincidunt ut laoreet dolore magna aliquam erat volutpat. Ut wisi enim ad minim veniam, quis nostrud exerci tation ullamcorper suscipit lobortis nisl ut aliquip ex ea commodo consequat.</p>
      <p>Consectetuer adipiscing elit, sed diam nonummy nibh euismod tincidunt ut laoreet dolore magna aliquam erat volutpat. Ut wisi enim ad minim veniam, quis nostrud exerci tation ullamcorper suscipit lobortis nisl ut aliquip ex ea commodo consequat. Consectetuer adipiscing elit, sed diam nonummy nibh euismod tincidunt ut laoreet dolore magna aliquam erat volutpat. Ut wisi enim ad minim veniam, quis nostrud exerci tation ullamcorper suscipit lobortis nisl ut aliquip ex ea commodo consequat.</p>
      <div class="closing">Sincerely Yours</div>
      <div class="signature">Thomas Avery</div>
    </section>

    <div class="footer-rule left"></div>
    <div class="footer-rule right"></div>

    <ul class="contact">
      <li><svg viewBox="0 0 24 24" aria-hidden="true"><path d="M6.6 10.8a15.1 15.1 0 0 0 6.6 6.6l2.2-2.2a1 1 0 0 1 1-.25 11.4 11.4 0 0 0 3.6.57 1 1 0 0 1 1 1V20a1 1 0 0 1-1 1A17 17 0 0 1 3 4a1 1 0 0 1 1-1h3.5a1 1 0 0 1 1 1c0 1.25.2 2.45.57 3.57a1 1 0 0 1-.25 1z"/></svg>628.555.0147</li>
      <li><svg viewBox="0 0 24 24" aria-hidden="true"><path d="M2 5h20v14H2z M2 5l10 8 10-8"/></svg>info@wrkmb.ca</li>
      <li><svg viewBox="0 0 24 24" aria-hidden="true"><circle cx="12" cy="12" r="10"/></svg>www.wrkmb.ca</li>
    </ul>

    <address class="address">
      38642 Marlowe Dr<br>
      Ashford, WA 48203-1957
    </address>
  </main>
</body>
</html>
```